Business card design needed

A mobile coffee, eats and treats van. We sell freshly ground Morlandi coffee, a selection of yummy things to eats, and lovely giftwares, including candles, scarfs, jewellery. We also have an online store where additional home and giftwares can be purchased
Updates

Thanks so much for all your efforts so far, I have received some great concepts.  Just wanted to send out a reminder that our concept is coffee, eats and treats (the treats being home and gift ware)  We have a mobile van and also an online store.  I dont want to make my business card too "busy" but at the same time I would like to give my potential customers something that will really excite and intrigue them...

Thank you everyone for your designs...I think I have made a decision...have just sent out a couple of questions.  I will be loading a new project shortly if you are interested?  Thanks, Helena

Industry/Entity Type

Store

Contact Information for Business Card

The Little Sparrow - Coffee, Eats & Treats
Helena Marquardt
0439 582 616
helena@thelittlesparrow.com.au
www.thelittlesparrow.com.au
www.facebook.com/thelittlesparrow
https://twitter.com/TheLittleSparrow

Requirements
Nice to have
• It would be good to have a rewards program on the back, we can tick off when prople buy coffee....5th coffee free...something like that...

It would also be good for the card to look like a gift tag....

```html
<!DOCTYPE html>
<html lang="en">
<head>
<meta charset="utf-8">
<title>The Little Sparrow – Rewards Card</title>
<link rel="stylesheet" href="https://fonts.googleapis.com/css2?family=Arimo:wght@400;700&display=swap">
<style>
  :root {
    --backdrop: #5b5c5c;
    --card: #f1f1e2;
    --bubble: #f8f9f1;
    --tan: #c3aa7c;
    --stamp-gold: #b9a76c;
    --sage: #a3c18f;
    --ink: #000000;
    --pill: #ffffff;
    --dot-navy: #3d5a98;
    --dot-aqua: #55c3d6;
  }
  * { margin: 0; padding: 0; box-sizing: border-box; }
  html, body {
    width: 1200px; height: 693px; overflow: hidden;
    background: var(--backdrop);
    font-family: "Arimo", Arial, sans-serif;
  }
  .card {
    position: absolute; left: 19px; top: 25px;
    width: 1162px; height: 653px;
    background: var(--card); border-radius: 52px;
  }
  .art { position: absolute; left: 0; top: 0; width: 1200px; height: 693px; }
  .line { position: absolute; left: 79px; line-height: 1; white-space: nowrap; }
  .holder-name { top: 235px; font-size: 43px; font-weight: 700; color: var(--tan); }
  .phone { top: 295px; font-size: 36px; font-weight: 700; color: var(--ink); }
  .email { top: 346px; font-size: 31px; color: var(--ink); }
  .website { top: 387px; font-size: 28px; font-weight: 700; color: var(--ink); }
  .handle {
    position: absolute; left: 79px; height: 62px;
    display: flex; align-items: center; gap: 16px;
    padding-right: 26px; background: var(--pill); border-radius: 31px;
    font-size: 32px; color: var(--tan); white-space: nowrap;
  }
  .handle-dot { width: 62px; height: 62px; border-radius: 50%; flex: none; }
  .handle.handle-page { top: 483px; }
  .handle.handle-page .handle-dot { background: var(--dot-navy); }
  .handle.handle-feed { top: 560px; }
  .handle.handle-feed .handle-dot { background: var(--dot-aqua); }
  .bubble-text {
    position: absolute; left: 626px; top: 104px;
    font-size: 25px; font-weight: 700; line-height: 28.5px;
    color: var(--sage); text-transform: uppercase; white-space: nowrap;
  }
  .free-label {
    position: absolute; left: 820px; top: 572px; width: 89px;
    text-align: right; font-size: 25px; font-weight: 700;
    line-height: 28px; color: var(--tan); text-transform: uppercase;
  }
</style>
</head>
<body>
  <div class="card"></div>

  <svg class="art" viewBox="0 0 1200 693" aria-hidden="true">
    <g class="speech-bubble" fill="#f8f9f1">
      <circle cx="694" cy="160" r="105"/>
      <path d="M522 264 L620 170 L650 230 Z"/>
    </g>
    <g class="stamps" fill="#fff" stroke="#000" stroke-width="3.5">
      <circle cx="960" cy="107" r="37"/><circle cx="1070" cy="107" r="37"/>
      <circle cx="960" cy="228" r="37"/><circle cx="1070" cy="228" r="37"/>
      <circle cx="960" cy="350" r="37"/><circle cx="1070" cy="350" r="37"/>
      <circle cx="960" cy="471" r="37"/><circle cx="1070" cy="471" r="37"/>
    </g>
    <g class="reward-stamps" fill="#fff" stroke="#b9a76c" stroke-width="3.5">
      <circle cx="960" cy="593" r="37"/><circle cx="1070" cy="593" r="37"/>
    </g>
    <g class="cup-icon" fill="#c3aa7c">
      <rect x="780" y="566" width="45" height="7" rx="1"/>
      <path d="M783 576 L822 576 L816 629 L789 629 Z"/>
    </g>
  </svg>

  <div class="bubble-text">Flash<br>this card<br>before<br>paying</div>

  <div class="line holder-name">Helena Marquardt</div>
  <div class="line phone">0439 582 616</div>
  <div class="line email">helena@thelittlesparrow.com.au</div>
  <div class="line website">www.thelittlesparrow.com.au</div>

  <div class="handle handle-page"><span class="handle-dot"></span>thelittlesparrow</div>
  <div class="handle handle-feed"><span class="handle-dot"></span>TheLittleSparrow</div>

  <div class="free-label">Free<br>cup</div>
</body>
</html>
```